Brightpath Orthodontics business card design

Need a business card design that reflects our re-branding (orthodontic office - braces) and a new partnership with a pediatric dental office. We would like to include "for adults and children" on the card as well so adults know they are welcome to get their braces here as well. Office design is modern and would like business card to reflect a modern type look. Here's the text we would like to be included on the card:

Darren Holloway, DDS, MSD
5214 West Maple Avenue, Suite 204
Mansfield, TX 76099
817-555-0143
www.brightpathortho.example
info@brightpathortho.example
Updates

Can we add the following to the existing designs? Darren Holloway, DDS, MSD 5214 West Maple Avenue, Suite 204 Mansfield, TX 76099 817-555-0143

Does anyone have any more vertical designs available? Thanks!

Industry/Entity Type

Dental

```html
<!DOCTYPE html>
<html lang="en">
<head>
<meta charset="utf-8">
<title>Brightpath Orthodontics – Business Cards</title>
<link rel="stylesheet" href="https://fonts.googleapis.com/css2?family=Open+Sans:wght@400;600;700;800&display=swap">
<style>
  :root {
    --canvas: #e9eaec;
    --card: #ffffff;
    --ink: #1f1f1f;
    --brand-blue: #1479c9;
    --brand-blue-deep: #0b63ad;
    --accent-orange: #f7941d;
    --muted: #8a8a8a;
    --photo-warm: #f0d9b8;
    --photo-rose: #e88aa6;
    --photo-light: #fbf3e6;
  }
  * { box-sizing: border-box; margin: 0; padding: 0; }
  html, body {
    width: 1200px; height: 1000px; overflow: hidden;
    background: var(--canvas);
    font-family: "Open Sans", Arial, sans-serif;
  }
  .stage {
    width: 1200px; height: 1000px;
    display: flex; justify-content: center; align-items: center; gap: 70px;
  }
  .card {
    position: relative;
    width: 340px; height: 580px;
    background: var(--card);
    border-radius: 16px;
    overflow: hidden;
    box-shadow: 0 10px 30px rgba(0,0,0,.12);
  }
  .brand {
    display: flex; align-items: center; gap: 14px;
    padding: 40px 30px 0;
  }
  .brand-mark {
    flex: none; width: 46px; height: 46px; border-radius: 50%;
    background: var(--brand-blue);
  }
  .brand-name {
    font-weight: 800; font-size: 27px; line-height: 1.08;
    color: var(--ink); letter-spacing: -.3px;
  }
  .identity { padding: 48px 30px 0; text-align: right; }
  .person-name { font-size: 25px; font-weight: 700; color: var(--brand-blue); }
  .credentials { font-size: 14px; font-weight: 700; color: var(--muted); margin-top: 2px; }
  .email { font-size: 14px; color: var(--muted); margin-top: 12px; }
  .contact-panel {
    position: absolute; left: 14px; right: 14px; bottom: 14px;
    height: 200px; border-radius: 12px;
    background: linear-gradient(160deg, var(--brand-blue), var(--brand-blue-deep));
    color: #fff; text-align: center;
    padding-top: 36px;
  }
  .contact-label { font-size: 17px; }
  .phone { font-size: 27px; font-weight: 700; color: var(--accent-orange); margin: 2px 0 12px; }
  .address { font-size: 15px; line-height: 1.45; }
  .url-pill {
    margin: 34px 26px 0;
    background: var(--brand-blue); color: #fff;
    border-radius: 20px; text-align: center;
    font-size: 15px; letter-spacing: 1px; padding: 8px 0;
  }
  .family-photo {
    position: absolute; left: 0; right: 0; bottom: 0; height: 330px;
    background: linear-gradient(135deg, var(--photo-light) 0%, var(--photo-warm) 45%, var(--photo-rose) 100%);
  }
</style>
</head>
<body>
<main class="stage">
  <section class="card card-front">
    <div class="brand">
      <span class="brand-mark"></span>
      <span class="brand-name">Brightpath<br>Orthodontics</span>
    </div>
    <div class="identity">
      <p class="person-name">Darren Holloway</p>
      <p class="credentials">DDS, MSD</p>
      <p class="email">info@brightpathortho.example</p>
    </div>
    <div class="contact-panel">
      <p class="contact-label">Contact us:</p>
      <p class="phone">817-555-0143</p>
      <p class="address">5214 West Maple Avenue, Suite 204<br>Mansfield, TX 76099</p>
    </div>
  </section>

  <section class="card card-back">
    <div class="brand">
      <span class="brand-mark"></span>
      <span class="brand-name">Brightpath<br>Orthodontics</span>
    </div>
    <p class="url-pill">www.brightpathortho.example</p>
    <div class="family-photo" role="img" aria-label="Photo of a smiling young girl hugging her smiling mother"></div>
  </section>
</main>
</body>
</html>
```